Looking to get a signage design to be put infront of our store/building.

We need a design of our building with an existing Logo ( uploads inc).

We sell stainless steel sinks and benches as our main line of business.
We also sell Cool Room Shelving, Chrome Wire Shelving, Shop Fittings and Wardrobe Solutions and need the building to reflect this.

We would like to include our Logo and note that the font of the building will require painting to best reflect our crisp clean logo.

I have attached our brochure so you can get a feel for who we are. We do not manufacture so items are here ready to go

Target Market(s)

Cafe and restaurant owners, medical industry, domestic kitchens

Font styles to use
Other font styles liked:
• Minimo font used

Colors
0054AA
0677BA
7BADD7
CADEEF
E8F1F8

Requirements
Nice to have
• Would possibly be nice to see some of our products in our brochure on the building

```html
<!DOCTYPE html>
<html lang="en">
<head>
<meta charset="utf-8">
<title>Harbour Line Stainless – Storefront Sign</title>
<link rel="stylesheet" href="https://fonts.googleapis.com/css2?family=Quicksand:wght@400&family=Arimo:wght@700&family=Roboto+Condensed:wght@400&display=swap">
<style>
  :root {
    --backdrop: #e4e6e8;
    --charcoal: #333436;
    --sign-blue: #1e96d4;
    --white: #ffffff;
    --steel-light: #c9ced3;
    --steel-dark: #8a9096;
  }
  * { box-sizing: border-box; margin: 0; padding: 0; }
  html, body { width: 1200px; height: 799px; overflow: hidden; }
  body { background: var(--backdrop); position: relative; }

  .sign {
    position: absolute;
    left: 40px; top: 200px;
    width: 1120px; height: 400px;
    box-shadow: 0 6px 18px rgba(0,0,0,0.18);
  }
  .sign__header {
    position: absolute; left: 0; top: 0;
    width: 100%; height: 180px;
    background: var(--charcoal);
    display: flex; align-items: center; justify-content: center;
  }
  .brand-name {
    font-family: "Quicksand", sans-serif;
    font-weight: 400;
    font-size: 34px;
    letter-spacing: 1px;
    color: var(--white);
    padding-top: 10px;
  }
  .sign__band {
    position: absolute; left: 0; top: 180px;
    width: 100%; height: 220px;
    background: var(--sign-blue);
  }
  .headline {
    position: absolute;
    left: 130px; top: 28px;
    width: 860px; height: 52px;
    background: var(--charcoal);
    color: var(--white);
    font-family: "Arimo", sans-serif;
    font-weight: 700;
    font-size: 32px;
    display: flex; align-items: center; justify-content: center;
    letter-spacing: 0.2px;
  }
  .product-list {
    position: absolute;
    list-style: none;
    font-family: "Roboto Condensed", sans-serif;
    font-size: 21px;
    color: var(--white);
  }
  .product-list li { position: absolute; white-space: nowrap; }
  .product-list li::before {
    content: "•";
    position: absolute; left: -30px;
  }
  .product-image {
    position: absolute;
    background: linear-gradient(180deg, var(--steel-light), var(--steel-dark));
    opacity: 0.85;
  }
  .product-image--bench { left: 168px; top: 114px; width: 108px; height: 72px; }
  .product-image--rack  { left: 865px; top: 95px;  width: 68px;  height: 98px; }
</style>
</head>
<body>
  <section class="sign">
    <header class="sign__header">
      <span class="brand-name">harbour line stainless</span>
    </header>
    <div class="sign__band">
      <h1 class="headline">WE SELL STAINLESS STEEL SINKS AND BENCHES</h1>

      <div class="product-image product-image--bench" role="img" aria-label="Stainless steel three-tier bench shelving"></div>

      <ul class="product-list">
        <li style="left:326px; top:119px;">COOL ROOM SHELVING</li>
        <li style="left:598px; top:119px;">CHROME WIRE SHELVING</li>
        <li style="left:369px; top:155px;">SHOP FITTINGS</li>
        <li style="left:568px; top:155px;">WARDROBE SOLUTIONS</li>
      </ul>

      <div class="product-image product-image--rack" role="img" aria-label="Chrome wire shelving unit on castors"></div>
    </div>
  </section>
</body>
</html>
```